Business card design needed

I run a Beautician studio (for 7 years now)
I offer
- Vestolin Body Sugaring
- Velumi Glow
- Nails
- Facials
- Manicure
- Foot Treatment
It might not be necessary to list all those treatments?
Maybe the link to the Website is sufficient?
I leave that up to you ...
(more info on www.BuffsAndBrowsByMarisol.com.au)
Vestolin BodySugaring is our biggest success, It replaces waxing.
I would like to incorporate the logo into the Business Card.
We had many complaints regarding our old Business Cards as the Phone Number was to small.
On the backside, we would like a "your next Appointment" section.
Looking forward to you Design, cheers ... Marisol
Buffs by Brows by Marisol
14 Merindo Cct 3912 Aldermoor
www.BuffsAndBrowsByMarisol.com.au
03 9418 2276

```html
<!DOCTYPE html>
<html lang="en">
<head>
<meta charset="utf-8">
<title>Buffs &amp; Brows by Marisol – Business Card</title>
<link href="https://fonts.googleapis.com/css2?family=Open+Sans:ital,wght@0,400;0,600;1,400;1,600;1,700&display=swap" rel="stylesheet">
<style>
  :root{
    --stage:#e8e5e1;
    --card:#ffffff;
    --ink:#2b2b2b;
    --ink-soft:#3a3a3a;
    --black:#000000;
    --grey:#8c8c8e;
    --grey-light:#b9b9bb;
    --rule:#bdbdbd;
    --sun:#f2a51f;
    --white:#ffffff;
  }
  *{box-sizing:border-box;margin:0;padding:0}
  html,body{width:914px;height:1200px;overflow:hidden}
  body{background:var(--stage);font-family:"Open Sans",Arial,sans-serif;color:var(--ink);position:relative}

  .card{position:absolute;width:799px;height:456px;background:var(--card);border-radius:24px;overflow:hidden;box-shadow:0 6px 14px rgba(0,0,0,.25)}
  .card--front{left:62px;top:113px}
  .card--back{left:58px;top:676px}

  .front__wave{position:absolute;left:0;top:0;width:799px;height:456px}
  .front__title{position:absolute;left:46px;top:42px;font-size:41px;font-weight:400;letter-spacing:1px;color:var(--ink-soft);white-space:nowrap}
  .front__web{position:absolute;left:56px;top:116px;font-size:20px;letter-spacing:3.6px;color:var(--ink);white-space:nowrap}
  .front__phone{position:absolute;left:46px;top:253px;font-size:26px;color:var(--ink)}
  .front__address{position:absolute;left:46px;top:301px;font-size:22px;color:var(--ink)}
  .label{font-weight:700;font-style:italic}

  .brand{position:absolute;text-align:center;font-weight:600;letter-spacing:2px;line-height:1.25}
  .brand__dot{display:block;margin:0 auto 10px;border-radius:50%;background:var(--sun)}
  .brand--front{left:550px;top:290px;width:230px;color:var(--white);font-size:22px}
  .brand--front .brand__dot{width:56px;height:56px}
  .brand--back{left:565px;top:24px;width:200px;color:var(--ink);font-size:19px}
  .brand--back .brand__dot{width:50px;height:50px}

  .hours{position:absolute;left:46px;top:40px}
  .hours__title{font-size:30px;font-weight:700;font-style:italic;letter-spacing:.5px;color:var(--ink-soft);margin-bottom:6px}
  .hours__line{font-size:24px;line-height:38px;color:var(--ink)}
  .back__rule{position:absolute;left:44px;top:178px;width:710px;border-top:1px solid var(--rule)}

  .appt__date{position:absolute;left:36px;top:222px;font-size:28px;color:var(--ink);white-space:nowrap}
  .blank{display:inline-block;border-bottom:2px solid var(--ink);vertical-align:baseline;height:1px}
  .appt__days{position:absolute;left:32px;top:313px;display:flex;font-size:24px;color:var(--ink)}
  .day{display:flex;align-items:center;margin-right:26px}
  .day:last-child{margin-right:0}
  .day__box{width:34px;height:34px;border:1.5px solid var(--ink);margin-right:18px}
  .back__note{position:absolute;left:0;width:100%;top:388px;text-align:center;font-size:19.5px;font-style:italic;color:var(--ink);white-space:nowrap}
</style>
</head>
<body>

<section class="card card--front">
  <svg class="front__wave" viewBox="0 0 799 456" aria-hidden="true">
    <path d="M0,338 C120,392 260,430 420,345 C560,265 680,190 799,162 L799,456 L0,456 Z" fill="var(--black)"/>
    <path d="M0,330 C150,395 300,390 440,318 C580,240 700,180 799,160 L799,172 C690,200 580,262 445,338 C300,415 150,420 0,355 Z" fill="var(--grey)"/>
    <path d="M0,372 C150,425 290,430 430,360 C300,448 130,440 0,400 Z" fill="var(--white)"/>
    <path d="M40,395 C170,440 290,430 400,375 C300,430 170,445 40,410 Z" fill="var(--grey-light)"/>
  </svg>
  <h1 class="front__title">BUFFS&amp;BROWS BY MARISOL</h1>
  <p class="front__web">www.BuffsAndBrowsByMarisol.com.au</p>
  <p class="front__phone"><span class="label">p :</span> 03 9418 2276</p>
  <p class="front__address"><span class="label">a :</span> 14 Merindo Cct, 3912 Aldermoor</p>
  <div class="brand brand--front"><span class="brand__dot"></span>Vestolin Body Sugaring</div>
</section>

<section class="card card--back">
  <div class="hours">
    <h2 class="hours__title">Hours of Operation</h2>
    <p class="hours__line">Mo to Fr -&nbsp; 7.00am - 8.00pm</p>
    <p class="hours__line">Sa - 8.00am - 5.00pm</p>
  </div>
  <div class="brand brand--back"><span class="brand__dot"></span>Vestolin Body Sugaring</div>
  <div class="back__rule"></div>

  <p class="appt__date">Date :<span class="blank" style="width:72px"></span> / <span class="blank" style="width:72px"></span> / <span class="blank" style="width:88px"></span> &nbsp;@ <span class="blank" style="width:72px"></span> : &nbsp;<span class="blank" style="width:90px"></span>am / pm</p>

  <div class="appt__days">
    <span class="day"><span class="day__box"></span>Mon.</span>
    <span class="day"><span class="day__box"></span>Tue.</span>
    <span class="day"><span class="day__box"></span>Wed.</span>
    <span class="day"><span class="day__box"></span>Thu.</span>
    <span class="day"><span class="day__box"></span>Fri.</span>
    <span class="day"><span class="day__box"></span>SAT.</span>
  </div>

  <p class="back__note">If you are unable to keep your appointment, please contact us as soon as possible</p>
</section>

</body>
</html>
```